Etikett Re-Design für Nahrungsergänzungsmittel
Zielgruppe
Entwicklung und Verkauf von Nahrungsergänzungsmittel
Aufgabenstellung
Re-Design unseres erfolgreichen Produkts Lumavexin.
Wichtig: Das Design für Lumavexin soll auch für alle anderen Produkte verwendet werden können, d.h. nur Farbe und Inhalt sollen dann künfitg angepasst werden.
--> Wenige Farben verwenden
Achtung: Die aktuelle Hauptfarbe Orange #f46f1f sollte in etwa beibehalten werden
Maße: 145 x 55 mm
Link zum aktuellen Design: https://kornwaldhaus.de/products/lumavexin-die-dravomil-alternative-z-b-bei-adhs
Eine dauerhafte Zusammenbarbeit mit dem Designer wird angestrebt.

```html
<!DOCTYPE html>
<html lang="de">
<head>
<meta charset="utf-8">
<title>Lumavexin – Etiketten</title>
<link rel="stylesheet" href="https://fonts.googleapis.com/css2?family=Montserrat:wght@400;500;600;700&family=Open+Sans:wght@400;600;700&display=swap">
<style>
  :root {
    --page: #f1f1f1;
    --paper: #ffffff;
    --ink: #3a3a3a;
    --muted: #6b6b6b;
    --title: #6f6f6f;
    --row-alt: #f3f3f3;
    --rule: #e2e2e2;
    --orange: #ea6f2a;
    --sand: #c6ab87;
    --slate: #8590ab;
  }
  * { box-sizing: border-box; margin: 0; padding: 0; }
  html, body { width: 672px; height: 1200px; overflow: hidden; }
  body {
    background: var(--page);
    font-family: "Open Sans", Arial, sans-serif;
    color: var(--ink);
    display: flex;
    flex-direction: column;
    align-items: center;
    justify-content: center;
    gap: 64px;
  }
  .label {
    position: relative;
    width: 640px;
    height: 243px;
    background: var(--paper);
    box-shadow: 0 1px 4px rgba(0,0,0,.18);
    overflow: hidden;
  }
  .label--orange { --accent: var(--orange); }
  .label--sand   { --accent: var(--sand); }
  .label--slate  { --accent: var(--slate); }

  /* supplement facts */
  .facts {
    position: absolute; left: 14px; top: 13px; width: 187px;
    border-collapse: collapse; font-size: 6.3px;
  }
  .facts th {
    background: var(--accent); color: #fff; font-weight: 700;
    height: 13.5px; text-align: left; padding: 0 5px;
    border-right: 1.5px solid #fff;
  }
  .facts th:nth-child(2), .facts th:nth-child(3) { text-align: center; }
  .facts th:last-child { border-right: 0; }
  .facts td { height: 14.7px; padding: 0 5px; border-right: 1.5px solid #fff; }
  .facts td:nth-child(2), .facts td:nth-child(3) { text-align: right; }
  .facts tr:nth-child(even) td { background: var(--row-alt); }
  .facts td:last-child { border-right: 0; }

  .small { position: absolute; left: 14px; width: 190px; font-size: 5.6px; line-height: 1.3; color: var(--ink); }
  .small b { font-weight: 700; }
  .footnote { top: 107px; font-size: 4.8px; }
  .ingredients { top: 129px; }
  .best-before { top: 154px; }

  .badges { position: absolute; left: 103px; top: 189px; display: flex; gap: 7px; }
  .badge { width: 28px; text-align: center; }
  .badge svg { width: 27px; height: 27px; display: block; margin: 0 auto; }
  .badge span { display: block; font-family: "Montserrat", sans-serif; font-size: 3.6px; font-weight: 700; color: var(--accent); margin-top: 3px; letter-spacing: .3px; white-space: nowrap; }

  /* centre panel */
  .brand-block {
    position: absolute; left: 272px; top: 0; width: 97px; height: 96px;
    background: var(--accent);
    display: flex; flex-direction: column; align-items: center; justify-content: center; gap: 8px;
  }
  .brand-block .dot { width: 20px; height: 20px; border-radius: 50%; border: 2px solid #fff; }
  .brand-name { font-family: "Montserrat", sans-serif; font-weight: 500; color: #fff; font-size: 11px; letter-spacing: .2px; }
  .product { position: absolute; left: 222px; width: 200px; text-align: center; font-family: "Montserrat", sans-serif; }
  .product-name { top: 133px; font-size: 25px; font-weight: 600; color: var(--title); letter-spacing: .3px; }
  .content { top: 180px; font-size: 6.6px; font-weight: 600; color: var(--accent); }
  .claim { top: 219px; font-size: 6.5px; font-weight: 500; color: var(--muted); }

  /* info column */
  .info { position: absolute; left: 440px; width: 185px; font-size: 5.6px; line-height: 1.55; color: var(--ink); }
  .info b { font-weight: 700; }
  .use { top: 18px; }
  .storage { top: 61px; }
  .notes { top: 96px; }
  .maker { top: 193px; }
  .mini-brand { position: absolute; left: 584px; top: 208px; display: flex; flex-direction: column; align-items: center; gap: 3px; }
  .mini-brand .dot { width: 11px; height: 11px; border-radius: 50%; border: 1.2px solid #9a9a9a; }
  .mini-brand span { font-family: "Montserrat", sans-serif; font-size: 6.2px; color: #9a9a9a; }
</style>
</head>
<body>

<!-- orange -->
<section class="label label--orange">
  <table class="facts">
    <tr><th>Supplement Facts</th><th>1 Kapsel</th><th>NRV*</th></tr>
    <tr><td>L-Tyrosin</td><td>200 mg</td><td>-</td></tr>
    <tr><td>5-Hydroxytryptophan</td><td>80 mg</td><td>-</td></tr>
    <tr><td>Zink</td><td>5 mg</td><td>50 %</td></tr>
    <tr><td>Vitamin B6</td><td>1 mg</td><td>71 %</td></tr>
    <tr><td>Chrom</td><td>20 µg</td><td>50 %</td></tr>
  </table>
  <p class="small footnote">*% der empfohlenen Tagesdosis in der EU / recommended daily intake according to the EU</p>
  <p class="small ingredients"><b>Zutaten:</b> Hydroxypropylmethylcellulose (Kapselhülle), L-Thyrosin, 5-Hydroxytryptopham, Zink, Vitamin B6, Chrom</p>
  <p class="small best-before"><b>Mindestens haltbar bis Ende:</b><br>Siehe Aufdruck auf dem Dosenboden</p>
  <div class="badges">
    <div class="badge"><svg viewBox="0 0 28 28"><circle cx="14" cy="14" r="12.5" fill="none" stroke="var(--accent)" stroke-width="1.5"/><path d="M12 7h4v3l2 3v9h-8v-9l2-3z" fill="var(--accent)"/><line x1="6" y1="22" x2="22" y2="6" stroke="var(--accent)" stroke-width="1.3"/></svg><span>DAIRY FREE</span></div>
    <div class="badge"><svg viewBox="0 0 28 28"><circle cx="14" cy="14" r="12.5" fill="none" stroke="var(--accent)" stroke-width="1.5"/><line x1="14" y1="7" x2="14" y2="22" stroke="var(--accent)" stroke-width="1.4"/><g fill="var(--accent)"><ellipse cx="11.5" cy="11" rx="2" ry="3"/><ellipse cx="16.5" cy="11" rx="2" ry="3"/><ellipse cx="11.5" cy="16" rx="2" ry="3"/><ellipse cx="16.5" cy="16" rx="2" ry="3"/></g><line x1="6" y1="22" x2="22" y2="6" stroke="var(--accent)" stroke-width="1.3"/></svg><span>GLUTEN FREE</span></div>
    <div class="badge"><svg viewBox="0 0 28 28"><circle cx="14" cy="14" r="12.5" fill="none" stroke="var(--accent)" stroke-width="1.5"/><path d="M8 8h3.5l2.5 8 2.5-8H20l-4.5 12h-3z" fill="var(--accent)"/></svg><span>VEGAN</span></div>
  </div>
  <div class="brand-block"><span class="dot"></span><span class="brand-name">kornwaldhaus</span></div>
  <p class="product product-name">Lumavexin</p>
  <p class="product content">Inhalt: 50 Kapseln 26 gr</p>
  <p class="product claim">Regulates Serotonin and Dopamin balance</p>
  <p class="info use"><b>Verzehrsempfehlung:</b> Erwachsene verzehren täglich morgens 1-2 Kapseln mit ausreichend Flüssigkeit und einem Snack. / Suggested Use: Adults take 1-2 capsules with sufficient liquid and a carbohydrate snack preferably in the morning.</p>
  <p class="info storage"><b>Aufbewahrung:</b> Vor Wärme und Feuchtigkeit schützen. Außerhalb der Reichweite von kleinen Kindern aufbewahren. / Store in a cool, dry place.</p>
  <p class="info notes"><b>Hinweise:</b> Die angegebene empfohlene tägliche Verzehrmenge darf nicht überschritten werden. Sprechen Sie stets mit Ihrem Arzt, bevor Sie Nahrungsergänzungsmittel einnehmen. Nahrungsergänzungsmittel sollten nicht als Ersatz für eine ausgewogene und abwechslungsreiche Ernährung verwendet werden. / Caution: Do not exceed recommended dosage. Consult your GP before taking food supplements. Should not be used as a substitute for balanced and varied diet.</p>
  <p class="info maker"><b>Hergestellt in Deutschland für:</b><br>Kornwaldhaus<br>84123 Lindenfeld, Deutschland<br>www.kornwaldhaus.de</p>
  <div class="mini-brand"><span class="dot"></span><span>kornwaldhaus</span></div>
</section>

<!-- sand -->
<section class="label label--sand">
  <table class="facts">
    <tr><th>Supplement Facts</th><th>1 Kapsel</th><th>NRV*</th></tr>
    <tr><td>L-Tyrosin</td><td>200 mg</td><td>-</td></tr>
    <tr><td>5-Hydroxytryptophan</td><td>80 mg</td><td>-</td></tr>
    <tr><td>Zink</td><td>5 mg</td><td>50 %</td></tr>
    <tr><td>Vitamin B6</td><td>1 mg</td><td>71 %</td></tr>
    <tr><td>Chrom</td><td>20 µg</td><td>50 %</td></tr>
  </table>
  <p class="small footnote">*% der empfohlenen Tagesdosis in der EU / recommended daily intake according to the EU</p>
  <p class="small ingredients"><b>Zutaten:</b> Hydroxypropylmethylcellulose (Kapselhülle), L-Thyrosin, 5-Hydroxytryptopham, Zink, Vitamin B6, Chrom</p>
  <p class="small best-before"><b>Mindestens haltbar bis Ende:</b><br>Siehe Aufdruck auf dem Dosenboden</p>
  <div class="badges">
    <div class="badge"><svg viewBox="0 0 28 28"><circle cx="14" cy="14" r="12.5" fill="none" stroke="var(--accent)" stroke-width="1.5"/><path d="M12 7h4v3l2 3v9h-8v-9l2-3z" fill="var(--accent)"/><line x1="6" y1="22" x2="22" y2="6" stroke="var(--accent)" stroke-width="1.3"/></svg><span>DAIRY FREE</span></div>
    <div class="badge"><svg viewBox="0 0 28 28"><circle cx="14" cy="14" r="12.5" fill="none" stroke="var(--accent)" stroke-width="1.5"/><line x1="14" y1="7" x2="14" y2="22" stroke="var(--accent)" stroke-width="1.4"/><g fill="var(--accent)"><ellipse cx="11.5" cy="11" rx="2" ry="3"/><ellipse cx="16.5" cy="11" rx="2" ry="3"/><ellipse cx="11.5" cy="16" rx="2" ry="3"/><ellipse cx="16.5" cy="16" rx="2" ry="3"/></g><line x1="6" y1="22" x2="22" y2="6" stroke="var(--accent)" stroke-width="1.3"/></svg><span>GLUTEN FREE</span></div>
    <div class="badge"><svg viewBox="0 0 28 28"><circle cx="14" cy="14" r="12.5" fill="none" stroke="var(--accent)" stroke-width="1.5"/><path d="M8 8h3.5l2.5 8 2.5-8H20l-4.5 12h-3z" fill="var(--accent)"/></svg><span>VEGAN</span></div>
  </div>
  <div class="brand-block"><span class="dot"></span><span class="brand-name">kornwaldhaus</span></div>
  <p class="product product-name">Lumavexin</p>
  <p class="product content">Inhalt: 50 Kapseln 26 gr</p>
  <p class="product claim">Regulates Serotonin and Dopamin balance</p>
  <p class="info use"><b>Verzehrsempfehlung:</b> Erwachsene verzehren täglich morgens 1-2 Kapseln mit ausreichend Flüssigkeit und einem Snack. / Suggested Use: Adults take 1-2 capsules with sufficient liquid and a carbohydrate snack preferably in the morning.</p>
  <p class="info storage"><b>Aufbewahrung:</b> Vor Wärme und Feuchtigkeit schützen. Außerhalb der Reichweite von kleinen Kindern aufbewahren. / Store in a cool, dry place.</p>
  <p class="info notes"><b>Hinweise:</b> Die angegebene empfohlene tägliche Verzehrmenge darf nicht überschritten werden. Sprechen Sie stets mit Ihrem Arzt, bevor Sie Nahrungsergänzungsmittel einnehmen. Nahrungsergänzungsmittel sollten nicht als Ersatz für eine ausgewogene und abwechslungsreiche Ernährung verwendet werden. / Caution: Do not exceed recommended dosage. Consult your GP before taking food supplements. Should not be used as a substitute for balanced and varied diet.</p>
  <p class="info maker"><b>Hergestellt in Deutschland für:</b><br>Kornwaldhaus<br>84123 Lindenfeld, Deutschland<br>www.kornwaldhaus.de</p>
  <div class="mini-brand"><span class="dot"></span><span>kornwaldhaus</span></div>
</section>

<!-- slate -->
<section class="label label--slate">
  <table class="facts">
    <tr><th>Supplement Facts</th><th>1 Kapsel</th><th>NRV*</th></tr>
    <tr><td>L-Tyrosin</td><td>200 mg</td><td>-</td></tr>
    <tr><td>5-Hydroxytryptophan</td><td>80 mg</td><td>-</td></tr>
    <tr><td>Zink</td><td>5 mg</td><td>50 %</td></tr>
    <tr><td>Vitamin B6</td><td>1 mg</td><td>71 %</td></tr>
    <tr><td>Chrom</td><td>20 µg</td><td>50 %</td></tr>
  </table>
  <p class="small footnote">*% der empfohlenen Tagesdosis in der EU / recommended daily intake according to the EU</p>
  <p class="small ingredients"><b>Zutaten:</b> Hydroxypropylmethylcellulose (Kapselhülle), L-Thyrosin, 5-Hydroxytryptopham, Zink, Vitamin B6, Chrom</p>
  <p class="small best-before"><b>Mindestens haltbar bis Ende:</b><br>Siehe Aufdruck auf dem Dosenboden</p>
  <div class="badges">
    <div class="badge"><svg viewBox="0 0 28 28"><circle cx="14" cy="14" r="12.5" fill="none" stroke="var(--accent)" stroke-width="1.5"/><path d="M12 7h4v3l2 3v9h-8v-9l2-3z" fill="var(--accent)"/><line x1="6" y1="22" x2="22" y2="6" stroke="var(--accent)" stroke-width="1.3"/></svg><span>DAIRY FREE</span></div>
    <div class="badge"><svg viewBox="0 0 28 28"><circle cx="14" cy="14" r="12.5" fill="none" stroke="var(--accent)" stroke-width="1.5"/><line x1="14" y1="7" x2="14" y2="22" stroke="var(--accent)" stroke-width="1.4"/><g fill="var(--accent)"><ellipse cx="11.5" cy="11" rx="2" ry="3"/><ellipse cx="16.5" cy="11" rx="2" ry="3"/><ellipse cx="11.5" cy="16" rx="2" ry="3"/><ellipse cx="16.5" cy="16" rx="2" ry="3"/></g><line x1="6" y1="22" x2="22" y2="6" stroke="var(--accent)" stroke-width="1.3"/></svg><span>GLUTEN FREE</span></div>
    <div class="badge"><svg viewBox="0 0 28 28"><circle cx="14" cy="14" r="12.5" fill="none" stroke="var(--accent)" stroke-width="1.5"/><path d="M8 8h3.5l2.5 8 2.5-8H20l-4.5 12h-3z" fill="var(--accent)"/></svg><span>VEGAN</span></div>
  </div>
  <div class="brand-block"><span class="dot"></span><span class="brand-name">kornwaldhaus</span></div>
  <p class="product product-name">Lumavexin</p>
  <p class="product content">Inhalt: 50 Kapseln 26 gr</p>
  <p class="product claim">Regulates Serotonin and Dopamin balance</p>
  <p class="info use"><b>Verzehrsempfehlung:</b> Erwachsene verzehren täglich morgens 1-2 Kapseln mit ausreichend Flüssigkeit und einem Snack. / Suggested Use: Adults take 1-2 capsules with sufficient liquid and a carbohydrate snack preferably in the morning.</p>
  <p class="info storage"><b>Aufbewahrung:</b> Vor Wärme und Feuchtigkeit schützen. Außerhalb der Reichweite von kleinen Kindern aufbewahren. / Store in a cool, dry place.</p>
  <p class="info notes"><b>Hinweise:</b> Die angegebene empfohlene tägliche Verzehrmenge darf nicht überschritten werden. Sprechen Sie stets mit Ihrem Arzt, bevor Sie Nahrungsergänzungsmittel einnehmen. Nahrungsergänzungsmittel sollten nicht als Ersatz für eine ausgewogene und abwechslungsreiche Ernährung verwendet werden. / Caution: Do not exceed recommended dosage. Consult your GP before taking food supplements. Should not be used as a substitute for balanced and varied diet.</p>
  <p class="info maker"><b>Hergestellt in Deutschland für:</b><br>Kornwaldhaus<br>84123 Lindenfeld, Deutschland<br>www.kornwaldhaus.de</p>
  <div class="mini-brand"><span class="dot"></span><span>kornwaldhaus</span></div>
</section>

</body>
</html>
```